starting a new business venture, need business cards and website friendly Logo. Professional, Classy, Unique!
(Need Creative)

Business Name:
BRAXMOREN Coaching and Capital Group

4193 Kestrel Bend Rd. Box 518
Larkfield, Westmere 43952
738-582-7309

www.braxmoren.com

Quote: Try and Fail but NEVER Fail to Try

```html
<!DOCTYPE html>
<html lang="en">
<head>
<meta charset="utf-8">
<title>BRAXMOREN Coaching and Capital Group – Business Card</title>
<link rel="stylesheet" href="https://fonts.googleapis.com/css2?family=Open+Sans:wght@400;600;700&display=swap">
<style>
  :root {
    --page: #f3ede4;
    --card-grey: #c3c3c6;
    --card-white: #ffffff;
    --slate: #3f4a5a;
    --blue: #1f6fd1;
    --blue-light: #3b8ff0;
    --navy: #2e3b4e;
    --brand-blue: #2456a8;
    --ink: #141414;
    --divider: #ffffff;
  }
  * { margin: 0; padding: 0; box-sizing: border-box; }
  html, body { width: 1200px; height: 800px; overflow: hidden; }
  body {
    background: var(--page);
    font-family: "Open Sans", Arial, sans-serif;
    position: relative;
  }
  .card {
    position: absolute;
    left: 320px;
    width: 560px;
    height: 330px;
    border-radius: 28px;
    overflow: hidden;
  }
  /* ---------- Front ---------- */
  .card-front { top: 50px; background: var(--slate); }
  .front-info {
    position: absolute; left: 0; top: 0;
    width: 296px; height: 100%;
    background: var(--card-grey);
  }
  .front-divider {
    position: absolute; left: 296px; top: 0;
    width: 8px; height: 100%;
    background: var(--divider);
  }
  .accent-strip {
    position: absolute; left: 55px; top: 0;
    width: 35px; height: 279px;
    background: var(--blue);
  }
  .accent-strip-foot {
    position: absolute; left: 55px; top: 279px;
    width: 35px; height: 51px;
    background: var(--navy);
  }
  .accent-tab {
    position: absolute; left: 50px; top: 33px;
    width: 44px; height: 74px;
    background: var(--blue-light);
    clip-path: polygon(0 10%, 100% 0, 100% 90%, 0 100%);
  }
  .person-name {
    position: absolute; left: 88px; top: 54px;
    font-size: 25px; font-weight: 700; color: var(--ink);
    letter-spacing: 0.2px;
  }
  .person-role {
    position: absolute; left: 88px; top: 86px;
    font-size: 17px; font-weight: 600; color: var(--ink);
  }
  .contact-row {
    position: absolute; left: 94px;
    font-size: 14px; color: var(--ink);
    line-height: 1.35;
  }
  .contact-row.address { font-size: 12px; }
  .contact-icon {
    position: absolute; left: 62px;
    width: 22px; height: 22px;
    border: 1.5px solid #fff;
    border-radius: 3px;
    display: flex; align-items: center; justify-content: center;
  }
  .front-brand {
    position: absolute; left: 304px; top: 0;
    width: 256px; height: 100%;
    display: flex; flex-direction: column;
    align-items: center; justify-content: center;
    color: #ffffff; font-weight: 700;
    text-align: center;
  }
  .front-brand .brand-name { font-size: 22px; letter-spacing: 0.5px; }
  .front-brand .brand-sub { font-size: 12px; margin-top: 4px; }
  .card-notch {
    position: absolute; right: -2px; top: 80px;
    width: 36px; height: 61px;
    background: var(--page);
    border-radius: 10px 0 0 10px;
  }
  /* ---------- Back ---------- */
  .card-back { top: 420px; background: var(--card-white); }
  .back-tab {
    position: absolute; left: 0; top: 30px;
    width: 212px; height: 22px;
    background: var(--brand-blue);
  }
  .back-tab-light {
    position: absolute; left: 10px; top: 27px;
    width: 60px; height: 26px;
    background: var(--blue-light);
  }
  .back-tab-end {
    position: absolute; left: 175px; top: 30px;
    width: 37px; height: 22px;
    background: var(--navy);
  }
  .back-brand {
    position: absolute; left: 0; top: 100px;
    width: 100%;
    text-align: center;
    color: var(--brand-blue); font-weight: 700;
  }
  .back-brand .brand-name { font-size: 36px; letter-spacing: 1px; line-height: 1.1; }
  .back-brand .brand-sub { font-size: 17px; margin-top: 4px; }
  .back-rule {
    position: absolute; left: 130px; top: 220px;
    width: 312px; height: 2px;
    background: var(--brand-blue);
  }
  .back-web {
    position: absolute; left: 0; top: 243px;
    width: 100%;
    display: flex; align-items: center; justify-content: center; gap: 10px;
    font-size: 17px; color: var(--slate);
    letter-spacing: 2px;
  }
  .back-web .web-mark {
    width: 18px; height: 18px; background: var(--slate); border-radius: 3px;
  }
</style>
</head>
<body>

<section class="card card-front" aria-label="Business card front">
  <div class="front-info"></div>
  <div class="accent-strip"></div>
  <div class="accent-strip-foot"></div>
  <div class="accent-tab"></div>

  <div class="person-name">YOUR NAME</div>
  <div class="person-role">Graphic Designer</div>

  <div class="contact-icon" style="top:166px">
    <svg width="14" height="14" viewBox="0 0 24 24"><path fill="#fff" d="M6.6 10.8a15.1 15.1 0 0 0 6.6 6.6l2.2-2.2c.3-.3.7-.4 1-.2 1.1.4 2.3.6 3.6.6.6 0 1 .4 1 1V20c0 .6-.4 1-1 1A17 17 0 0 1 3 4c0-.6.4-1 1-1h3.5c.6 0 1 .4 1 1 0 1.3.2 2.5.6 3.6.1.3 0 .7-.2 1z"/></svg>
  </div>
  <div class="contact-row" style="top:168px">738-582-7309</div>

  <div class="contact-icon" style="top:203px">
    <svg width="14" height="14" viewBox="0 0 24 24" fill="none" stroke="#fff" stroke-width="2"><circle cx="12" cy="12" r="9"/><path d="M3 12h18M12 3c3 3 3 15 0 18M12 3c-3 3-3 15 0 18"/></svg>
  </div>
  <div class="contact-row" style="top:205px">www.braxmoren.com</div>

  <div class="contact-icon" style="top:244px">
    <svg width="14" height="14" viewBox="0 0 24 24"><path fill="#fff" d="M12 2a7 7 0 0 0-7 7c0 5 7 13 7 13s7-8 7-13a7 7 0 0 0-7-7zm0 9.5A2.5 2.5 0 1 1 12 6.5a2.5 2.5 0 0 1 0 5z"/></svg>
  </div>
  <div class="contact-row address" style="top:240px">4193 Kestrel Bend Rd. Box 518<br>Larkfield, Westmere 43952</div>

  <div class="front-divider"></div>
  <div class="front-brand">
    <div class="brand-name">BRAXMOREN</div>
    <div class="brand-sub">Coaching and Capital Group</div>
  </div>
  <div class="card-notch"></div>
</section>

<section class="card card-back" aria-label="Business card back">
  <div class="back-tab"></div>
  <div class="back-tab-light"></div>
  <div class="back-tab-end"></div>

  <div class="back-brand">
    <div class="brand-name">BRAXMOREN</div>
    <div class="brand-sub">Coaching and Capital Group</div>
  </div>
  <div class="back-rule"></div>
  <div class="back-web"><span class="web-mark"></span>www.braxmoren.com</div>
</section>

</body>
</html>
```